Design a Consultation and HR Services Website "Shift Pathways"

Consultation and HR Services
I am looking for a design gives the look and feel of Varden Calloway and Ferrovane
we need a high-quality graphics website that looks rich and expensive.
we are working as an affiliate for international consultation firms and sole agent for international HR products.
we are a group of consultants for the Middle East.
we will get the global practices to local practices.

Reason: I am not getting enough options and designs. I am not getting what I was looking for in matter of look and feel. looking for something rich and luxury with black background and rich font. www.blockvault.example www.lucindavarga.example 71dormerplace.example/ www.velquo.example/rd/en/ morvethhouse.example/ www.velquo.example/rd/en/ www.quillen.example/ www.theplaudits.example/ .

Target Market(s)

Corporate all size and industries in GCC

Industry/Entity Type

Management Consulting

Coding

Coded - Design and coding required

Number of Pages Required

5+ page

Font styles to use
Sans Serif
Script

Colors
ffffff
ecf7fb
cee9f5
85cae6
33a6d7
0592cd
000000
848484

Requirements
Must have
• This is the looks and feel that I'm looking for.
• http://www.blockvault.example/?channel=display&subchannel=sitemuse
• http://www.lucindavarga.example/lvny-private/en/
• http://71dormerplace.example/
• http://www.velquo.example/rd/en/
• http://morvethhouse.example/
• http://www.quillen.example/
• http://www.theplaudits.example/
• Home
• Who we are?
• What we do?
• HR & OD Consultation
• Executive Coaching
• Assesment Cemter
• HRIS & Outsourcing
• Testimonials
• Our Partners
• Contact Us
• We need support on Technical righting...

```html
<!DOCTYPE html>
<html lang="en">
<head>
<meta charset="utf-8">
<title>Shift Pathways — Consultation and HR Services</title>
<link href="https://fonts.googleapis.com/css2?family=Open+Sans:wght@400;600;700;800&display=swap" rel="stylesheet">
<style>
:root{
  --black:#000000;
  --ink:#0b0d10;
  --panel:#15181c;
  --white:#ffffff;
  --ice:#ecf7fb;
  --mist:#cee9f5;
  --sky:#85cae6;
  --blue:#33a6d7;
  --deep-blue:#0592cd;
  --grey:#848484;
  --line:#2a2e33;
}
*{margin:0;padding:0;box-sizing:border-box}
html,body{width:857px;height:1200px;overflow:hidden;background:var(--black)}
body{font-family:"Open Sans",Arial,sans-serif;color:var(--white);position:relative}
a{color:inherit;text-decoration:none}

/* header */
.site-header{position:absolute;top:0;left:0;width:857px;height:46px;background:var(--black);border-bottom:2px solid var(--deep-blue)}
.brand{position:absolute;left:22px;top:8px;display:flex;align-items:center;gap:8px}
.brand-dot{width:28px;height:28px;border-radius:50%;background:var(--deep-blue)}
.brand-name{font-size:17px;font-weight:700;color:var(--white)}
.social-row{position:absolute;right:22px;top:5px;display:flex;gap:4px}
.social-row span{width:11px;height:11px;background:var(--grey);border-radius:2px}
.main-nav{position:absolute;right:22px;top:24px;display:flex;font-size:8px;font-weight:700;letter-spacing:.4px}
.main-nav a{padding:4px 9px;border-left:1px solid var(--grey);color:var(--white)}
.main-nav a:first-child{border-left:none;color:var(--sky);border-bottom:2px solid var(--deep-blue)}

/* hero */
.hero{position:absolute;top:46px;left:0;width:857px;height:310px}
.hero-photo{position:absolute;inset:0;background:linear-gradient(180deg,#f2f3f4 0%,#dfe1e3 55%,#b9bcbf 100%)}
.hero-caption{position:absolute;left:100px;top:232px;background:rgba(255,255,255,.88);padding:8px 14px;color:#151515;font-weight:800;font-size:17px;line-height:22px;letter-spacing:.3px}
.hero-dots{position:absolute;left:100px;top:290px;display:flex;gap:5px}
.hero-dots span{width:7px;height:7px;border-radius:50%;background:var(--grey)}
.hero-dots span:first-child{background:var(--deep-blue)}

/* welcome */
.welcome{position:absolute;top:356px;left:0;width:857px;height:160px;background:linear-gradient(180deg,#111315,#060708);text-align:center}
.emblem{position:absolute;left:416px;top:-12px;width:26px;height:26px;border-radius:50%;background:var(--black);border:2px solid var(--deep-blue)}
.welcome h1{margin-top:24px;font-size:22px;font-weight:800;letter-spacing:.5px}
.welcome p{width:700px;margin:10px auto 0;font-size:7.5px;line-height:11px;color:#c9ccd0}
.btn-light{display:inline-block;margin-top:10px;background:var(--white);color:#111;font-size:7px;font-weight:600;padding:4px 12px}

/* services */
.services{position:absolute;top:516px;left:0;width:857px;height:312px;text-align:center}
.services-photo{position:absolute;inset:0;background:linear-gradient(160deg,#0c2130 0%,#081521 45%,#0f3144 80%,#0a1a26 100%)}
.services h2{position:relative;margin-top:22px;font-size:24px;font-weight:700}
.services .sub{position:relative;font-size:8px;color:#b8c4cc;margin-top:2px}
.service-grid{position:relative;display:flex;justify-content:center;gap:22px;margin-top:26px}
.service{width:160px}
.service-icon{width:60px;height:60px;border-radius:50%;background:var(--deep-blue);border:3px solid var(--sky);margin:0 auto;display:flex;align-items:center;justify-content:center}
.service h3{font-size:10.5px;font-weight:700;margin-top:12px}
.service p{font-size:7px;line-height:10px;color:#c5ced4;margin-top:6px}

/* testimonials & partners */
.lower{position:absolute;top:828px;left:0;width:857px;height:244px;background:var(--ink)}
.col-title{font-size:15px;font-weight:700;padding-bottom:6px;border-bottom:1px solid var(--line)}
.testimonials{position:absolute;left:78px;top:24px;width:320px}
.client-photo{position:absolute;left:0;top:40px;width:68px;height:68px;border-radius:50%;background:linear-gradient(160deg,#e8d9c6,#b79a80);border:2px solid var(--white)}
.quote{position:absolute;left:80px;top:40px;width:238px;font-size:7px;line-height:10px;color:#c9ccd0}
.quote cite{display:block;margin-top:6px;font-style:normal;color:var(--sky)}
.more-link{position:absolute;right:0;top:150px;font-size:7px;color:var(--white);border-bottom:1px solid var(--deep-blue)}
.partners{position:absolute;left:452px;top:24px;width:325px}
.partner-box{position:absolute;top:40px;left:0;width:325px;height:100px;background:var(--white);display:flex;align-items:center;justify-content:center;gap:44px}
.partner-mark{width:70px;height:40px;background:#d7dbe0;border-radius:3px}
.partner-mark.alt{width:40px;border-radius:50%;background:#c9d0d6}
.arrows{position:absolute;right:0;top:148px;display:flex;gap:4px}
.arrows span{width:14px;height:14px;background:#2b2f34;display:flex;align-items:center;justify-content:center}

/* footer */
.site-footer{position:absolute;top:1072px;left:0;width:857px;height:114px;background:#050607;border-top:1px solid var(--line)}
.foot-col{position:absolute;top:14px}
.foot-col h4{font-size:9.5px;font-weight:700;margin-bottom:8px}
.quick-links{left:24px}
.quick-links li{list-style:none;font-size:6.5px;color:#b8bdc2;line-height:10px}
.quick-links li::before{content:"› ";color:var(--blue)}
.newsletter{left:168px;width:140px}
.newsletter p{font-size:6.5px;color:#b8bdc2}
.field{height:14px;background:#1b1f23;border:1px solid var(--line);margin-top:8px}
.contact{left:338px;width:170px}
.contact-row{display:flex;gap:6px;align-items:flex-start;font-size:6.5px;color:#b8bdc2;line-height:9px;margin-bottom:6px}
.contact-row i{flex:none;width:12px;height:12px;border-radius:50%;background:var(--deep-blue);display:flex;align-items:center;justify-content:center}
.footer-name{position:absolute;right:40px;top:40px;font-size:26px;font-weight:700;color:#1d3a4a}
.footer-social{position:absolute;right:24px;bottom:10px;display:flex;gap:4px}
.footer-social span{width:11px;height:11px;background:var(--grey);border-radius:2px}
.copyright{position:absolute;bottom:0;left:0;width:857px;height:14px;background:var(--black);font-size:6px;color:var(--grey);padding:3px 24px}
</style>
</head>
<body>

<header class="site-header">
  <a class="brand" href="#"><span class="brand-dot"></span><span class="brand-name">Shift Pathways</span></a>
  <div class="social-row"><span></span><span></span><span></span><span></span><span></span></div>
  <nav class="main-nav">
    <a href="#">HOME</a><a href="#">WHO WE ARE?</a><a href="#">WHAT WE DO?</a><a href="#">TESTIMONIALS</a><a href="#">OUR PARTNERS</a><a href="#">CONTACT US</a>
  </nav>
</header>

<section class="hero">
  <div class="hero-photo" role="img" aria-label="Chess pieces on a board, a red king standing out among white pawns"></div>
  <h2 class="hero-caption">WE ARE A COMPANY OFFERING<br>CONSULTATION AND HR SERVICES</h2>
  <div class="hero-dots"><span></span><span></span><span></span><span></span></div>
</section>

<section class="welcome">
  <span class="emblem"></span>
  <h1>WELCOME TO SHIFT PATHWAYS</h1>
  <p>We are a group of consultants serving the Middle East, working as an affiliate for international consultation firms and as sole agent for international HR products. We bring proven global practices into local practice, helping organisations of every size and industry across the GCC grow their people, sharpen their structures and lead change with confidence and care.</p>
  <a class="btn-light" href="#">Read More</a>
</section>

<section class="services">
  <div class="services-photo" role="img" aria-label="City skyline at night in deep blue tones"></div>
  <h2>What We Do?</h2>
  <p class="sub">Global practice, delivered with local understanding.</p>
  <div class="service-grid">
    <div class="service">
      <div class="service-icon"><svg width="30" height="26" viewBox="0 0 30 26" fill="#fff"><circle cx="15" cy="7" r="5"/><path d="M5 25c0-7 4-10 10-10s10 3 10 10z"/><circle cx="5" cy="9" r="3"/><circle cx="25" cy="9" r="3"/></svg></div>
      <h3>HR &amp; OD Consultation</h3>
      <p>Structures, policies and people plans built to match your goals and your culture.</p>
    </div>
    <div class="service">
      <div class="service-icon"><svg width="32" height="22" viewBox="0 0 32 22" fill="none" stroke="#fff" stroke-width="2.5" stroke-linejoin="round"><path d="M2 8l7-5 7 4 7-4 7 5-9 9-5-4-5 4z"/></svg></div>
      <h3>Executive Coaching</h3>
      <p>One to one coaching that helps leaders think clearly and act with lasting impact.</p>
    </div>
    <div class="service">
      <div class="service-icon"><svg width="28" height="26" viewBox="0 0 28 26" fill="#fff"><rect x="2" y="14" width="5" height="10"/><rect x="11" y="8" width="5" height="16"/><rect x="20" y="2" width="5" height="22"/></svg></div>
      <h3>Assessment Centre</h3>
      <p>Fair, tested assessment tools to select, develop and promote the right talent.</p>
    </div>
    <div class="service">
      <div class="service-icon"><svg width="28" height="28" viewBox="0 0 28 28" fill="none" stroke="#fff" stroke-width="3"><circle cx="14" cy="14" r="6"/><path d="M14 2v5M14 21v5M2 14h5M21 14h5M5.5 5.5l3.5 3.5M19 19l3.5 3.5M5.5 22.5L9 19M19 9l3.5-3.5"/></svg></div>
      <h3>HRIS &amp; Outsourcing</h3>
      <p>Modern HR systems and managed services that free your team to focus.</p>
    </div>
  </div>
</section>

<section class="lower">
  <div class="testimonials">
    <h3 class="col-title">Client Testimonials</h3>
    <div class="client-photo" role="img" aria-label="Portrait of a client"></div>
    <blockquote class="quote">Working with the team changed how we hire and grow our people. Their advice was practical, clear and tailored to our region, and the results showed within months across every department we serve.
      <cite>— Rania Haddad, HR Director</cite>
    </blockquote>
    <a class="more-link" href="#">Read more testimonials</a>
  </div>
  <div class="partners">
    <h3 class="col-title">Our Partners</h3>
    <div class="partner-box">
      <span class="partner-mark"></span>
      <span class="partner-mark alt"></span>
    </div>
    <div class="arrows">
      <span><svg width="6" height="8" viewBox="0 0 6 8"><path d="M5 1L1 4l4 3" stroke="#fff" fill="none"/></svg></span>
      <span><svg width="6" height="8" viewBox="0 0 6 8"><path d="M1 1l4 3-4 3" stroke="#fff" fill="none"/></svg></span>
    </div>
  </div>
</section>

<footer class="site-footer">
  <div class="foot-col quick-links">
    <h4>Quick Links</h4>
    <ul><li>Home</li><li>Who We Are?</li><li>What We Do?</li><li>Testimonials</li><li>Our Partners</li><li>Contact Us</li></ul>
  </div>
  <div class="foot-col newsletter">
    <h4>Newsletter Signup</h4>
    <p>Get our latest insights sent to your inbox.</p>
    <div class="field"></div>
    <div class="field"></div>
  </div>
  <div class="foot-col contact">
    <h4>Contact Info</h4>
    <div class="contact-row"><i><svg width="6" height="8" viewBox="0 0 6 8"><path d="M3 8S0 4.5 0 3a3 3 0 016 0C6 4.5 3 8 3 8z" fill="#fff"/></svg></i><span>Office 12, Tower Road, Business Bay, Dubai, UAE</span></div>
    <div class="contact-row"><i><svg width="7" height="7" viewBox="0 0 7 7"><path d="M1 0h2l1 2-1 1a4 4 0 002 2l1-1 2 1v1a1 1 0 01-1 1C3 7 0 4 0 1a1 1 0 011-1z" fill="#fff"/></svg></i><span>+971 4 000 0000</span></div>
    <div class="contact-row"><i><svg width="7" height="5" viewBox="0 0 7 5"><rect x=".5" y=".5" width="6" height="4" fill="none" stroke="#fff"/><path d="M.5.5l3 2 3-2" stroke="#fff" fill="none"/></svg></i><span>info@shiftpathways.example</span></div>
  </div>
  <div class="footer-name">Shift Pathways</div>
  <div class="footer-social"><span></span><span></span><span></span><span></span><span></span></div>
</footer>
<div class="copyright">Copyright 2015 Shift Pathways. All Rights Reserved.</div>

</body>
</html>
```